brightquokka.net we need a webpage designed for our new product

We need a webpage designed for our new range of products from our new brand. We have had a logo designed on sketchharbor (see attached) and we want to keep to this theme. Our first product is a range of affordable app controlled LED lightbulbs.

I have added some photos that we think is good inspirational material and would be good as a background to this website, but we want the site to look modern but not conventional. We would like something that makes our company look quirky not corporate.

Thats it

Target Market(s)

Our product is being stocked by big name online retailers in the UK, the page will get link through hits from our app. Our target market is gadget freaks of all ages.

Industry/Entity Type

It Company

Requirements
Must have
• We are going to need a help page, text to be uploaded next few days.

We need a contact page.

design my work on iOS and Android as most people will access page through their handset or tablet.
Should not have
• We do not want anything too corporate.

```html
<!DOCTYPE html>
<html lang="en">
<head>
<meta charset="utf-8">
<title>Bright Quokka – App Controlled LED Lightbulbs</title>
<link rel="stylesheet" href="https://fonts.googleapis.com/css2?family=Aldrich&family=Lato:wght@400;700&display=swap">
<style>
  :root{
    --green:#45ad4a;
    --green-dark:#3f9f32;
    --green-mid:#6cb62a;
    --lime:#a6e03a;
    --lime-bar:#c6f55a;
    --ink:#2e2e2e;
    --grey:#555;
    --grey-light:#8a8a7e;
    --white:#fff;
  }
  *{margin:0;padding:0;box-sizing:border-box}
  html,body{width:903px;height:1200px;overflow:hidden;background:var(--white)}
  body{position:relative;font-family:"Lato",sans-serif;color:var(--ink)}
  .abs{position:absolute}

  /* header */
  .site-header{left:0;top:0;width:903px;height:63px;background:var(--green);z-index:2}
  .nav-link{position:absolute;top:0;height:63px;line-height:61px;font-family:"Aldrich",sans-serif;font-size:12px;letter-spacing:.5px;color:var(--white);text-transform:uppercase}
  .nav-link.active{top:8px;height:45px;line-height:43px;width:81px;text-align:center;border:1px solid var(--white)}
  .brand-box{left:335px;top:0;width:234px;height:106px;background:var(--white);z-index:3;display:flex;align-items:flex-end;justify-content:center;padding-bottom:12px}
  .brand-name{font-family:"Aldrich",sans-serif;font-size:16px;letter-spacing:.5px;color:var(--green);text-transform:uppercase}

  /* background texture */
  .texture{left:0;top:322px;width:903px;height:606px;background:linear-gradient(180deg,#fafad8 0%,#fdfde4 50%,#f3f5c4 58%,#e7eca2 70%,#e3e99a 85%,#ebedaa 100%)}

  /* hero */
  .hero-photo{left:0;top:63px;width:903px;height:259px;background:linear-gradient(100deg,#6d6a45 0%,#8c8455 30%,#a89a68 55%,#7b6f49 80%,#5f5a3c 100%)}
  .product-photo{left:315px;top:150px;width:275px;height:235px;background:linear-gradient(160deg,#f2f2ee 0%,#cfd0cc 60%,#2b2b2b 100%);z-index:2}
  .slide-arrow{top:166px;width:44px;height:44px;z-index:2}
  .slide-dots{left:672px;top:342px;display:flex;gap:9px;z-index:2}
  .dot{width:15px;height:15px;border-radius:50%;border:1.5px solid #444;background:var(--white)}
  .dot.current{background:var(--green);border-color:var(--green)}

  /* intro */
  .intro{left:0;top:410px;width:903px;text-align:center}
  .intro-kicker{font-family:"Aldrich",sans-serif;font-size:19px;color:var(--ink);line-height:30px}
  .intro-product{font-family:"Aldrich",sans-serif;font-size:35px;color:var(--green);line-height:44px}
  .intro-title{font-family:"Aldrich",sans-serif;font-weight:400;font-size:28px;color:var(--grey);line-height:48px}
  .intro-copy{width:740px;margin:20px auto 0;font-size:14px;line-height:18px;color:var(--grey-light)}
  .intro-copy b{color:var(--ink);font-weight:700}

  /* feature circles */
  .feature{top:701px;width:200px;height:200px;border-radius:50%;text-align:center;color:var(--white);padding-top:68px}
  .feature h2{font-family:"Aldrich",sans-serif;font-weight:400;font-size:27px;line-height:34px;margin-bottom:6px}
  .feature p{font-size:14px;line-height:17px}
  .feature.shop{left:107px;background:var(--green-dark)}
  .feature.blog{left:356px;background:var(--lime);color:var(--ink)}
  .feature.new{left:605px;background:var(--green-mid)}

  /* footer */
  .footer-heading{font-family:"Aldrich",sans-serif;font-weight:400;font-size:21px;color:var(--ink);letter-spacing:.5px}
  .contact-line{font-family:"Aldrich",sans-serif;color:var(--ink)}
  .phone{font-size:18px;letter-spacing:1px}
  .small{font-family:"Aldrich",sans-serif;font-size:12px;color:var(--grey);letter-spacing:.5px;line-height:20px}
  .footer-brand{left:360px;top:1137px;width:200px;text-align:center;font-family:"Aldrich",sans-serif;font-size:13px;color:var(--green);text-transform:uppercase}
  .hours-day{font-family:"Aldrich",sans-serif;font-size:17px;color:var(--green);letter-spacing:1px}
  .hours-time{font-family:"Aldrich",sans-serif;font-size:17px;color:var(--ink);letter-spacing:1px}
  .legal-bar{left:0;top:1165px;width:903px;height:35px;background:var(--lime-bar);text-align:center;line-height:35px;font-size:11px;color:var(--grey)}
</style>
</head>
<body>

<div class="abs texture" role="img" aria-label="Soft yellow and green grunge texture background"></div>

<header class="abs site-header">
  <nav>
    <span class="nav-link active" style="left:18px">Home</span>
    <span class="nav-link" style="left:135px">New</span>
    <span class="nav-link" style="left:221px">About us</span>
    <span class="nav-link" style="left:619px">Toys</span>
    <span class="nav-link" style="left:697px">Gadgets</span>
    <span class="nav-link" style="left:800px">Contact</span>
  </nav>
</header>
<div class="abs brand-box"><span class="brand-name">Brightquokka</span></div>

<div class="abs hero-photo" role="img" aria-label="Photo of a crowded shop full of vintage toys and collectible figures"></div>
<div class="abs product-photo" role="img" aria-label="Product photo of app controlled LED bulbs, remote, hub, tablet and phones"></div>

<svg class="abs slide-arrow" style="left:31px" viewBox="0 0 44 44" aria-label="Previous slide">
  <rect x="8" y="8" width="28" height="28" transform="rotate(45 22 22)" fill="#111" stroke="#fff" stroke-width="2.5"/>
  <path d="M29 22H15M20 17l-5 5 5 5" fill="none" stroke="#fff" stroke-width="1.6"/>
</svg>
<svg class="abs slide-arrow" style="left:818px" viewBox="0 0 44 44" aria-label="Next slide">
  <rect x="8" y="8" width="28" height="28" transform="rotate(45 22 22)" fill="#111" stroke="#fff" stroke-width="2.5"/>
  <path d="M15 22h14M24 17l5 5-5 5" fill="none" stroke="#fff" stroke-width="1.6"/>
</svg>
<div class="abs slide-dots">
  <span class="dot"></span><span class="dot current"></span><span class="dot"></span><span class="dot"></span>
</div>

<section class="abs intro">
  <p class="intro-kicker">Huge range of affordable app controlled</p>
  <p class="intro-product">LED lightbulbs</p>
  <h1 class="intro-title">Welcome to Bright Quokka</h1>
  <p class="intro-copy">Duis autem vel eum iriure dolor in hendrerit in vulputate velit esse molestie consequat, vel illum dolore eu feugiat nulla facilisis at vero eros et accumsan. Duis autem vel eum iriure dolor in hendrerit in vulputate velit esse molestie consequat, vel illum dolore eu feugiat nulla facilisis at vero eros et accumsan.Lorem ipsum dolor sit amet, consectetuer adipiscing elit, sed diam nonummy nibh euismod tincidunt ut laoreet.Vulputate velit esse molestie consequa...<b>READMORE</b></p>
</section>

<a class="abs feature shop"><h2>Our Shop</h2><p>Let's Visit our Shop<br>Online!</p></a>
<a class="abs feature blog"><h2>Blog</h2><p>What our Customers<br>talk about us!</p></a>
<a class="abs feature new"><h2>New</h2><p>Check out what's<br>new in Stock</p></a>

<footer>
  <h3 class="abs footer-heading" style="left:65px;top:957px">Contact us</h3>
  <svg class="abs" style="left:65px;top:1010px" width="44" height="38" viewBox="0 0 44 38" aria-hidden="true">
    <rect x="2" y="2" width="40" height="34" fill="none" stroke="#45ad4a" stroke-width="3"/>
    <circle cx="14" cy="14" r="4" fill="#45ad4a"/>
    <path d="M7 28c0-6 14-6 14 0z" fill="#45ad4a"/>
    <path d="M25 12h12M25 19h12M25 26h8" stroke="#45ad4a" stroke-width="3"/>
  </svg>
  <p class="abs contact-line phone" style="left:128px;top:1010px">Tlf. 00 11 22 33</p>
  <p class="abs small" style="left:128px;top:1032px">Info@brightquokka.net</p>
  <svg class="abs" style="left:72px;top:1078px" width="28" height="44" viewBox="0 0 28 44" aria-hidden="true">
    <path d="M14 2C7 2 2 7 2 14c0 9 12 22 12 22s12-13 12-22C26 7 21 2 14 2z" fill="#45ad4a"/>
    <circle cx="14" cy="14" r="4.5" fill="#fff"/>
    <ellipse cx="14" cy="40" rx="11" ry="3" fill="none" stroke="#45ad4a" stroke-width="2"/>
  </svg>
  <p class="abs contact-line" style="left:133px;top:1074px;font-size:14px;letter-spacing:1px">Bright Quokka</p>
  <p class="abs small" style="left:128px;top:1094px">Elm Row, Leeds<br>England, UK.</p>

  <p class="abs footer-brand">Brightquokka</p>

  <h3 class="abs footer-heading" style="left:654px;top:957px">Opening hours</h3>
  <p class="abs hours-day" style="left:655px;top:1011px">TUE – FRI.</p>
  <p class="abs hours-time" style="left:655px;top:1032px">9:00 &nbsp;– &nbsp;18:00</p>
  <p class="abs hours-day" style="left:655px;top:1077px">SAT</p>
  <p class="abs hours-time" style="left:655px;top:1099px">10:00 &nbsp;– &nbsp;15:00</p>

  <div class="abs legal-bar">© 2014 BRIGHT QUOKKA &nbsp;| &nbsp;ALL RIGHTS RESERVED</div>
</footer>

</body>
</html>
```